Compelling Marketing page for Photo Services

We are a membership-based photo services company and we are looking for a eye-catching marketing page that incorporates our flagship product of a budget plan of photo printing every month with our new addition of a member rewards plan.

The existing design can be found at http://www.snapnestle.example/75glossies/perks.php.

This page is the basic layout for the marketing page and the form can not be deviated from too greatly, however we are looking for new innovative ideas on promoting this value to our potential customers.

If you need further clarification or more information please contact us.
Updates

Thank you for your comments.  I've updated the brief to include a file with the logo on it in EPS format.  If you need another format, please ask.  The link for the existing campaign is http://www.snapnestle.example/75glossies/perks.php.

Target Market(s)

Our target market is generally female averages 45-50. Income is low to medium.

Industry/Entity Type

Marketing

Requirements
Must have
• The registration form can not change in terms of content - look and placement can vary according to design.
Nice to have
• Inclusion of our new member rewards program. $500 reward dollars for new signups and 100 reward dollars every month thereafter.
Should not have
• Can not say "free" or "guaranteed"

```html
<!DOCTYPE html>
<html lang="en">
<head>
<meta charset="utf-8">
<title>snapnestle – Sign Up</title>
<link rel="stylesheet" href="https://fonts.googleapis.com/css2?family=Arimo:wght@400;700&family=Marcellus&family=Open+Sans:wght@400;600;700&family=Libre+Baskerville:wght@400;700&display=swap">
<style>
  :root{
    --orange:#f7931e;
    --orange-deep:#e8760a;
    --ink:#222222;
    --grey-text:#3c3c3c;
    --heading-grey:#4a4a4a;
    --panel:#1e1e1e;
    --panel-text:#dddddd;
    --field:#3b3b3b;
    --field-edge:#5a5a5a;
    --rule:#d9d9d9;
    --white:#ffffff;
  }
  *{box-sizing:border-box;margin:0;padding:0}
  html,body{width:1195px;height:1200px;overflow:hidden;background:var(--white)}
  .page{position:relative;width:1000px;height:1000px;transform:scale(1.195,1.2);transform-origin:0 0;font-family:"Arimo",Arial,sans-serif;color:var(--grey-text)}
  .abs{position:absolute}

  /* header */
  .brand{left:22px;top:52px;display:flex;align-items:center;gap:12px}
  .brand-square{width:30px;height:30px;background:var(--orange)}
  .brand-name{font-family:"Open Sans",sans-serif;font-weight:700;font-size:50px;color:var(--ink);letter-spacing:-1px;line-height:1}
  .tagline{left:415px;top:40px;font-family:"Marcellus",serif;font-style:italic;font-size:26px;color:var(--ink)}
  .offer{left:515px;top:70px;display:flex;align-items:baseline;gap:12px}
  .offer-number{font-family:"Libre Baskerville",serif;font-weight:700;font-size:56px;color:var(--orange)}
  .offer-text{font-family:"Marcellus",serif;font-size:24px;color:var(--ink)}
  .lens{left:880px;top:0;width:120px;height:108px;border-radius:0 0 0 60px;background:radial-gradient(circle at 55% 50%,#6a3a70 0,#1a1a2a 35%,#111 60%,#555 100%)}
  .header-rule{left:0;top:155px;width:1000px;height:2px;background:var(--orange)}

  /* hero */
  .hero{left:0;top:157px;width:1000px;height:298px;background:linear-gradient(90deg,#6b5f52 0%,#a8998a 35%,#4a4139 70%,#2a2420 100%)}
  .hero-caption{left:0;top:404px;width:625px;height:51px;background:rgba(20,20,20,.75);color:var(--white);font-family:"Open Sans",sans-serif;font-weight:600;font-size:25px;padding:10px 0 0 15px}

  /* form */
  .signup{left:625px;top:245px;width:353px;height:692px;background:var(--panel);border-radius:0 0 14px 14px}
  .ribbon{left:600px;top:205px;width:390px;height:40px;z-index:2}
  .ribbon-label{left:648px;top:208px;z-index:3;color:var(--white);font-family:"Open Sans",sans-serif;font-weight:600;font-size:27px}
  .box{width:13px;height:13px;background:#5c5c5c;border:1px solid #888}
  .fine{color:var(--panel-text);font-size:12px;line-height:18px;text-align:justify;letter-spacing:.3px}
  .field-label{width:100px;text-align:right;color:var(--panel-text);font-size:12.5px;letter-spacing:.2px}
  .field{height:19px;background:var(--field);border:1px solid var(--field-edge)}
  .select{height:20px;background:var(--field);border:1px solid var(--field-edge);display:flex;justify-content:flex-end;align-items:center;color:var(--panel-text);font-size:11px}
  .select span{margin-right:auto;padding-left:4px}
  .select i{width:15px;height:16px;background:#111;margin-right:1px;display:flex;align-items:center;justify-content:center}
  .dob-note{left:659px;top:626px;color:var(--panel-text);font-size:12.5px;line-height:17px;letter-spacing:.3px}
  .dob-note strong{color:var(--orange)}
  .consent{left:665px;top:719px;width:302px;color:var(--panel-text);font-size:12px;line-height:16px;letter-spacing:.35px}
  .consent u{color:var(--panel-text)}
  .submit{left:719px;top:848px;width:161px;height:34px;background:linear-gradient(#fb9a35,var(--orange-deep));border:1px solid #b85a00;color:var(--white);font-family:"Open Sans",sans-serif;font-weight:600;font-size:15px;display:flex;align-items:center;justify-content:center}

  /* benefits */
  .benefits-title{left:0;width:630px;top:492px;text-align:center;font-family:"Open Sans",sans-serif;font-weight:700;font-size:24px;color:var(--heading-grey)}
  .benefits-title span{color:var(--orange)}
  .rule-v{left:313px;top:530px;width:1px;height:405px;background:var(--rule)}
  .rule-h{left:110px;top:737px;width:420px;height:1px;background:var(--rule)}
  .benefit-title{font-family:"Marcellus",serif;font-weight:400;font-size:16px;color:var(--orange);white-space:nowrap}
  .benefit-text{font-size:12px;line-height:16px;color:var(--grey-text);letter-spacing:.45px}
  .learn{font-size:11px;font-weight:700;color:var(--orange);letter-spacing:.5px}
  .icon{border-radius:4px}
</style>
</head>
<body>
<div class="page">
  <header>
    <div class="abs brand"><span class="brand-square"></span><span class="brand-name">snapnestle</span></div>
    <p class="abs tagline">Sign Up with snapnestle &amp; get</p>
    <p class="abs offer"><span class="offer-number">100</span><span class="offer-text">6x4 Prints Each Month.</span></p>
    <div class="abs lens" role="img" aria-label="Close-up photo of a camera lens"></div>
    <div class="abs header-rule"></div>
  </header>

  <section>
    <div class="abs hero" role="img" aria-label="Sepia photo of three smiling children sitting outdoors"></div>
    <p class="abs hero-caption">Exclusive access to our personal photo service.</p>
  </section>

  <section class="signup-form">
    <div class="abs signup"></div>
    <svg class="abs ribbon" viewBox="0 0 390 40" aria-hidden="true">
      <polygon points="0,0 390,0 390,40 25,40 12,20" fill="#f7931e"/>
      <polygon points="0,0 25,40 25,48" fill="#a85800"/>
    </svg>
    <p class="abs ribbon-label">Sign Up Today!</p>

    <span class="abs box" style="left:643px;top:265px"></span>
    <p class="abs fine" style="left:665px;top:262px;width:288px">By checking this box you authorize us to use your saved information from your registration to take advantage of this offer.</p>

    <span class="abs field-label" style="left:640px;top:337px">First Name:</span><span class="abs field" style="left:754px;top:333px;width:163px"></span>
    <span class="abs field-label" style="left:640px;top:369px">Last Name:</span><span class="abs field" style="left:754px;top:368px;width:163px"></span>
    <span class="abs field-label" style="left:640px;top:401px">Street Address:</span><span class="abs field" style="left:754px;top:399px;width:163px"></span>
    <span class="abs field-label" style="left:640px;top:433px">Suite / Apt. No:</span><span class="abs field" style="left:754px;top:431px;width:163px"></span>
    <span class="abs field-label" style="left:640px;top:465px">Zip Code:</span><span class="abs field" style="left:754px;top:463px;width:60px"></span>
    <span class="abs field-label" style="left:640px;top:497px">City:</span><span class="abs field" style="left:754px;top:495px;width:163px"></span>
    <span class="abs field-label" style="left:640px;top:529px">State:</span>
    <span class="abs select" style="left:754px;top:527px;width:47px"><span>XX</span><i><svg width="8" height="5"><polygon points="0,0 8,0 4,5" fill="#fff"/></svg></i></span>
    <span class="abs field-label" style="left:640px;top:561px">Phone (Resi):</span>
    <span class="abs field" style="left:754px;top:559px;width:54px"></span><span class="abs field" style="left:813px;top:559px;width:54px"></span><span class="abs field" style="left:872px;top:559px;width:54px"></span>
    <span class="abs field-label" style="left:640px;top:593px">E-mail:</span><span class="abs field" style="left:754px;top:591px;width:163px"></span>

    <p class="abs dob-note">Please enter your <strong>date of birth</strong><br>for security verification purposes.</p>
    <span class="abs field-label" style="left:640px;top:674px">Date of Birth:</span>
    <span class="abs select" style="left:754px;top:672px;width:42px"><i><svg width="8" height="5"><polygon points="0,0 8,0 4,5" fill="#fff"/></svg></i></span>
    <span class="abs select" style="left:811px;top:672px;width:42px"><i><svg width="8" height="5"><polygon points="0,0 8,0 4,5" fill="#fff"/></svg></i></span>
    <span class="abs select" style="left:868px;top:672px;width:52px"><i><svg width="8" height="5"><polygon points="0,0 8,0 4,5" fill="#fff"/></svg></i></span>

    <span class="abs box" style="left:643px;top:720px"></span>
    <p class="abs consent">By clicking the "<strong>Click here to Submit</strong>" button below, I confirm the information submitted and that I am 18 years old or older and are duly authorized by the tele-phone account owner to make changes to and incur charges on this telephone bill account provided. Further I confirm my understanding and approval of the <u>Terms &amp; Conditions</u> and <u>Privacy Policy</u> of this offer.</p>
    <div class="abs submit">Click Here to Submit</div>
  </section>

  <section class="benefits">
    <h2 class="abs benefits-title">More Benefits of <span>snapnestle Include:</span></h2>
    <div class="abs rule-v"></div>
    <div class="abs rule-h"></div>

    <h3 class="abs benefit-title" style="left:49px;top:580px">Email Service</h3>
    <div class="abs icon" style="left:167px;top:550px;width:55px;height:52px;background:linear-gradient(#fbd8a8,var(--orange))" role="img" aria-label="Envelope with an at sign illustration"></div>
    <p class="abs benefit-text" style="left:49px;top:608px;width:225px">Unlimited email messaging with an easy to use address book and sorting functions. snapnestle also provides a spam filter that effectively keeps out junk mail from your inbox.</p>
    <span class="abs learn" style="left:204px;top:692px">Learn More...</span>

    <h3 class="abs benefit-title" style="left:342px;top:577px">Member Rewards</h3>
    <div class="abs icon" style="left:484px;top:556px;width:42px;height:44px;background:linear-gradient(#7fd3e6,#1c8fb0)" role="img" aria-label="Address book with phone illustration"></div>
    <p class="abs benefit-text" style="left:339px;top:604px;width:242px">As a valued snapnestle member you earn $500 reward dollars upon sign up and $100 additional rewards dollars each month you are an active member. You can use rewards dollars towards the purchase of gift cards to your favorite stores.</p>
    <span class="abs learn" style="left:497px;top:700px">Learn More...</span>

    <h3 class="abs benefit-title" style="left:51px;top:784px">Print Your Memories</h3>
    <div class="abs icon" style="left:222px;top:760px;width:60px;height:48px;background:linear-gradient(#444,#111)" role="img" aria-label="Digital photo frame illustration"></div>
    <p class="abs benefit-text" style="left:54px;top:813px;width:236px">Select individual pictures or whole albums and easily add them to your cart for printing. Our members recieve 100 prints each month, shipping and handling included!</p>
    <span class="abs learn" style="left:208px;top:895px">Learn More...</span>

    <h3 class="abs benefit-title" style="left:344px;top:780px">Quality Prints</h3>
    <div class="abs icon" style="left:466px;top:760px;width:60px;height:44px;background:linear-gradient(135deg,#e0503a,#e9c046 50%,#3a9a4a)" role="img" aria-label="Stack of colourful photo prints illustration"></div>
    <p class="abs benefit-text" style="left:339px;top:808px;width:228px">With our high-gloss, bright white, resin-coated photo paper.Our built-in software will also notify you prior to order if we see a problem with the resolution so you know you can expect the best looking photos.</p>
    <span class="abs learn" style="left:497px;top:899px">Learn More...</span>
  </section>
</div>
</body>
</html>
```